Heritage Australian brand needs new packaging design to reflect the change to being 100% Recycled.

The heritage Australian brand - KLOVA™ Fabric Combs have been sold to households worldwide (but mostly Australia) for over 40 years.

It was invented in Sydney in 1970, and since then many imitations are in the marketplace have copied it exactly. (colour, print colour) In fact, KLOVA™ comb is a generic word for a fabric comb in the marketplace.

Our KLOVA™ Fabric Comb will be a world first 100% recycled product that will be a different colour - Hex #606f61 or RGB 9611197, or as per Duraclad steel colour Wildnerness.

We need it to be differentiated from the "old" blue plastic to the new "green". sustainable product.

We need a design that is modern, yet retro/traditional, that takes us into a new era.

It sits with our other tool - the Super KLOVA™ Fabric Comb that is already sustainably produced. (wooden handle, brass teeth, Australian steel)

Both combs are locally produced in Melbourne, Australia.

We need this for a calico bag that has 2 sizes.
Small: 110mm x 90mm (fits the small KLOVA™)
Large: 250mm x 300mm - also has smaller inner pocket 100mm x 70mm to hold BOTH combs, seperately so they don't blunt the brass teeth.
The back of each of these bags has the Instructions on it, as well as logos - Kestrel Mark etc.

We also need Card Packaging designed for each of the Combs.

We have trademarked the KLOVA™ logo and use the font Flash Bold.

We will want to add gift boxing later, so ideally the design can be easily transferred across different packaging options.

The final design should communicate heritage, honesty, stability, and integrity. (Think of Pelvin toothpaste, Dorrat mustard, Klingmoor Vattlund is our aspirational competitor)

Also lean towards simple and bold design. In the original brief, I mention Pelvin Toothpaste. Not in a design sense, but in the modern yet tradtional packaging. The KLOVA™ Comb is such a simple tool, that I think a colourblock or simple bold design would align. KISS principle.

```html
<!DOCTYPE html>
<html lang="en">
<head>
<meta charset="utf-8">
<title>KLOVA Fabric Comb – Packaging Options</title>
<link href="https://fonts.googleapis.com/css2?family=Montserrat:wght@400;500;700;800&family=Oswald:wght@500&family=Raleway:wght@500&family=Hind:wght@400;600&display=swap" rel="stylesheet">
<style>
  :root{
    --green:#606f61;
    --paper:#f8f7f3;
    --page:#ffffff;
    --ghost:#eeede8;
    --shadow:0 1px 4px rgba(0,0,0,.18);
  }
  *{margin:0;padding:0;box-sizing:border-box}
  html,body{width:1200px;height:1200px;overflow:hidden;background:var(--page)}
  .board{position:relative;width:1200px;height:1200px;color:var(--green)}
  .option-title{position:absolute;font-family:"Montserrat",sans-serif;font-weight:500;font-size:41px;line-height:1;transform:translateX(-50%);white-space:nowrap;letter-spacing:.5px}
  .panel{position:absolute;background:var(--paper);box-shadow:var(--shadow);overflow:hidden}
  .wordmark{font-family:"Montserrat",sans-serif;font-weight:800;color:var(--green);line-height:1;letter-spacing:.02em;white-space:nowrap}
  .wordmark sup{font-weight:400;font-size:.3em;vertical-align:top;margin-left:.1em;letter-spacing:0}
  .tagline{font-family:"Oswald",sans-serif;font-weight:500;text-transform:uppercase;text-align:center;line-height:1.15;letter-spacing:-.02em;white-space:nowrap}
  .origin{font-family:"Raleway",sans-serif;font-weight:500;white-space:nowrap}

  /* option 1 front */
  .front-framed .frame{position:absolute;left:49px;top:52px;width:158px;height:210px;border:1.3px solid var(--green)}
  .front-framed .wordmark{position:absolute;left:0;right:0;top:128px;text-align:center;font-size:27px}
  .front-framed .tagline{position:absolute;left:0;right:0;top:164px;font-size:11px}
  .front-framed .origin{position:absolute;left:0;right:0;top:243px;text-align:center;font-size:7.5px}

  /* option 2 front */
  .pattern-strip{position:absolute;left:0;top:0;width:81px;height:100%;background:linear-gradient(90deg,#d9dbd6,#c9cdc8 50%,#d9dbd6)}
  .front-patterned .brand{position:absolute;left:95px;top:78px;width:120px;text-align:center}
  .front-patterned .wordmark{font-size:27px}
  .front-patterned .tagline{font-size:11px;margin-top:11px}
  .front-patterned .origin{position:absolute;left:101px;top:243px;font-size:7.5px}
  .mandala-arc{position:absolute;left:71px;bottom:0;width:116px;height:40px;border-radius:58px 58px 0 0;background:radial-gradient(ellipse at 50% 100%,#8c978d,#b4bbb4 70%,#d4d8d3)}

  /* option 3 front */
  .front-banded .band{position:absolute;left:0;top:0;width:131px;height:100%;background:var(--green)}
  .front-banded .wordmark{position:absolute;left:64px;top:401px;color:var(--paper);font-size:76px;transform:translate(-50%,-50%) rotate(-90deg)}
  .front-banded .frame{position:absolute;left:166px;top:160px;width:259px;height:78px;border:1.5px solid var(--green);display:flex;align-items:center;justify-content:center}
  .front-banded .tagline{font-size:22.5px;line-height:1.05}
  .front-banded .origin{position:absolute;left:167px;top:529px;font-size:15px}

  /* back panel info block */
  .back-info{position:absolute;left:50%;transform:translateX(-50%);width:20.5em;text-align:center;font-family:"Hind",sans-serif}
  .back-info .headline{font-family:"Montserrat",sans-serif;font-weight:400;font-size:.92em;line-height:1.15;white-space:nowrap;padding-bottom:.5em;border-bottom:1px solid var(--green)}
  .back-info .headline b{font-weight:700}
  .badges{display:flex;justify-content:space-between;padding:.75em 0 .3em;border-bottom:1px solid var(--green)}
  .badge{width:6.6em;display:flex;flex-direction:column;align-items:center}
  .badge svg{width:3.6em;height:3.6em}
  .badge span{font-size:.66em;line-height:1.25;margin-top:.55em}
  .uses{font-size:.8em;line-height:1.3;padding-top:.55em}
  .uses b,.usage b{font-weight:600}
  .usage{font-size:.8em;line-height:1.45;padding:.5em 0 .9em;border-bottom:1px solid var(--green)}
  .socials{display:flex;justify-content:center;gap:1.4em;padding:.75em 0;border-bottom:1px solid var(--green)}
  .socials span{font-family:"Montserrat",sans-serif;font-weight:700;font-size:.6em;letter-spacing:.03em}
  .site{font-family:"Montserrat",sans-serif;font-size:.8em;letter-spacing:.1em;padding-top:.55em}
  .back-small .back-info{font-size:8.4px;top:51px}
  .back-large .back-info{font-size:17px;top:103px}
  .ghost-mark{position:absolute;left:50%;bottom:-30px;transform:translateX(-50%);color:var(--ghost);font-size:118px}
</style>
</head>
<body>
<div class="board">

  <h2 class="option-title" style="left:325px;top:53px">Option 1</h2>
  <h2 class="option-title" style="left:881px;top:53px">Option 2</h2>
  <h2 class="option-title" style="left:603px;top:472px">Option 3</h2>

  <!-- Option 1 -->
  <section class="panel front-framed" style="left:61px;top:118px;width:256px;height:313px">
    <div class="frame"></div>
    <div class="wordmark">KLOVA<sup>TM</sup></div>
    <div class="tagline">The heritage lint comb<br>made to last</div>
    <div class="origin">Made in Australia</div>
  </section>

  <section class="panel back-small" style="left:332px;top:118px;width:256px;height:313px">
    <div class="back-info">
      <p class="headline">The <b>KLOVA Fabric Combs</b> easily remove<br>pet hair, fuzz balls, lint, dust + pilling</p>
      <div class="badges">
        <div class="badge"><svg viewBox="0 0 100 100"><circle cx="50" cy="50" r="46" fill="none" stroke="currentColor" stroke-width="4"/><path d="M24 50 L43 68 L78 22" fill="none" stroke="currentColor" stroke-width="9" stroke-linecap="round" stroke-linejoin="round"/></svg><span>Lifetime Guarantee</span></div>
        <div class="badge"><svg viewBox="0 0 100 100"><circle cx="50" cy="50" r="46" fill="none" stroke="currentColor" stroke-width="4"/><circle cx="50" cy="50" r="28" fill="currentColor"/></svg><span>Kestrel Mark</span></div>
        <div class="badge"><svg viewBox="0 0 100 100"><circle cx="50" cy="50" r="46" fill="none" stroke="currentColor" stroke-width="4"/><path d="M50 88 V48" stroke="currentColor" stroke-width="4"/><path d="M50 46 C40 36 42 22 50 14 C58 22 60 36 50 46Z M48 56 C38 44 26 44 18 48 C26 60 38 62 48 56Z M52 56 C62 44 74 44 82 48 C74 60 62 62 52 56Z" fill="currentColor"/></svg><span>Environmentally<br>Friendly</span></div>
      </div>
      <p class="uses"><b>Use on:</b> Woollens and knits<br>Cotton and cashmere<br>Acrylics and polyester blends<br>Suede garments<br>Felt hats<br>Furnishing fabrics<br>Carpets, rugs and blankets</p>
      <p class="usage"><b>Great for:</b> Laundry, car, lounge, desk, travel<br><b>To use:</b> Comb firmly in one direction</p>
      <div class="socials"><span>Lensly</span><span>Circlo</span><span>Pinvo</span><span>Vidzy</span></div>
      <p class="site">www.klovacombworks.com</p>
    </div>
  </section>

  <!-- Option 2 -->
  <section class="panel front-patterned" style="left:619px;top:118px;width:257px;height:313px">
    <div class="pattern-strip" role="img" aria-label="Vertical band of geometric circle and petal line pattern"></div>
    <div class="brand">
      <div class="wordmark">KLOVA<sup>TM</sup></div>
      <div class="tagline">The heritage lint comb<br>made to last</div>
    </div>
    <div class="origin">Made in Australia</div>
  </section>

  <section class="panel back-small" style="left:890px;top:118px;width:256px;height:313px">
    <div class="back-info">
      <p class="headline">The <b>KLOVA Fabric Combs</b> easily remove<br>pet hair, fuzz balls, lint, dust + pilling</p>
      <div class="badges">
        <div class="badge"><svg viewBox="0 0 100 100"><circle cx="50" cy="50" r="46" fill="none" stroke="currentColor" stroke-width="4"/><path d="M24 50 L43 68 L78 22" fill="none" stroke="currentColor" stroke-width="9" stroke-linecap="round" stroke-linejoin="round"/></svg><span>Lifetime Guarantee</span></div>
        <div class="badge"><svg viewBox="0 0 100 100"><circle cx="50" cy="50" r="46" fill="none" stroke="currentColor" stroke-width="4"/><circle cx="50" cy="50" r="28" fill="currentColor"/></svg><span>Kestrel Mark</span></div>
        <div class="badge"><svg viewBox="0 0 100 100"><circle cx="50" cy="50" r="46" fill="none" stroke="currentColor" stroke-width="4"/><path d="M50 88 V48" stroke="currentColor" stroke-width="4"/><path d="M50 46 C40 36 42 22 50 14 C58 22 60 36 50 46Z M48 56 C38 44 26 44 18 48 C26 60 38 62 48 56Z M52 56 C62 44 74 44 82 48 C74 60 62 62 52 56Z" fill="currentColor"/></svg><span>Environmentally<br>Friendly</span></div>
      </div>
      <p class="uses"><b>Use on:</b> Woollens and knits<br>Cotton and cashmere<br>Acrylics and polyester blends<br>Suede garments<br>Felt hats<br>Furnishing fabrics<br>Carpets, rugs and blankets</p>
      <p class="usage"><b>Great for:</b> Laundry, car, lounge, desk, travel<br><b>To use:</b> Comb firmly in one direction</p>
      <div class="socials"><span>Lensly</span><span>Circlo</span><span>Pinvo</span><span>Vidzy</span></div>
      <p class="site">www.klovacombworks.com</p>
    </div>
    <div class="mandala-arc" role="img" aria-label="Half mandala dot ornament rising from the bottom edge"></div>
  </section>

  <!-- Option 3 -->
  <section class="panel front-banded" style="left:61px;top:533px;width:527px;height:633px">
    <div class="band"></div>
    <div class="wordmark">KLOVA<sup>TM</sup></div>
    <div class="frame"><div class="tagline">The heritage lint comb<br>made to last</div></div>
    <div class="origin">Made in Australia</div>
  </section>

  <section class="panel back-large" style="left:619px;top:533px;width:527px;height:633px">
    <div class="wordmark ghost-mark" aria-hidden="true">KLOVA<sup>TM</sup></div>
    <div class="back-info">
      <p class="headline">The <b>KLOVA Fabric Combs</b> easily remove<br>pet hair, fuzz balls, lint, dust + pilling</p>
      <div class="badges">
        <div class="badge"><svg viewBox="0 0 100 100"><circle cx="50" cy="50" r="46" fill="none" stroke="currentColor" stroke-width="4"/><path d="M24 50 L43 68 L78 22" fill="none" stroke="currentColor" stroke-width="9" stroke-linecap="round" stroke-linejoin="round"/></svg><span>Lifetime Guarantee</span></div>
        <div class="badge"><svg viewBox="0 0 100 100"><circle cx="50" cy="50" r="46" fill="none" stroke="currentColor" stroke-width="4"/><circle cx="50" cy="50" r="28" fill="currentColor"/></svg><span>Kestrel Mark</span></div>
        <div class="badge"><svg viewBox="0 0 100 100"><circle cx="50" cy="50" r="46" fill="none" stroke="currentColor" stroke-width="4"/><path d="M50 88 V48" stroke="currentColor" stroke-width="4"/><path d="M50 46 C40 36 42 22 50 14 C58 22 60 36 50 46Z M48 56 C38 44 26 44 18 48 C26 60 38 62 48 56Z M52 56 C62 44 74 44 82 48 C74 60 62 62 52 56Z" fill="currentColor"/></svg><span>Environmentally<br>Friendly</span></div>
      </div>
      <p class="uses"><b>Use on:</b> Woollens and knits<br>Cotton and cashmere<br>Acrylics and polyester blends<br>Suede garments<br>Felt hats<br>Furnishing fabrics<br>Carpets, rugs and blankets</p>
      <p class="usage"><b>Great for:</b> Laundry, car, lounge, desk, travel<br><b>To use:</b> Comb firmly in one direction</p>
      <div class="socials"><span>Lensly</span><span>Circlo</span><span>Pinvo</span><span>Vidzy</span></div>
      <p class="site">www.klovacombworks.com</p>
    </div>
  </section>

</div>
</body>
</html>
```